7 Herons Distillery - Bottle Label Design

We are a small craft distillery whose branding needs to incorporate our location on a lake (Lac Vernisse, Quebec, Canada). A unique aspect of the lake is that people drive floating docks on the lake powered by a small outboard motor (see photos). Back in the 1970’s when Lac Vernisse was a sparsely populated and difficult-to-access lake in the Gatineau Hills north of Ottawa, the concept of motorized docks was conjured on a lazy afternoon and this single stroke of genius has inadvertently spawned the most exceptional and eccentric lake based community. Throughout the summer, somewhere around four o’clock on any given Friday and Saturday it starts to happen. Docks set sail from their customary landing places - family, friends, snacks and loaded drink coolers in-tow and, as if magnetically drawn, head toward Pine Shoal. Without fail they will come upon a gathering of similar minded floating docks within the vicinity - be guided in with help to moor alongside and within seconds be seamlessly immersed in the festivities. Seldom any longer are these events planned, they have become elemental, a thing organically derived from within the community. This on-going weekly event is the genesis of the strong bond that brings us Seven Herons Distilling.
Each of the 4 distillery owners have one of these docks so hence the name. We are open to either "7 Herons" or spelled out as "Seven Herons" as may be visually appropriate. We are also open to "Distillery" or "Distilling". More detail on the docks themselves, they are 14x16 feet powered by a small outboard motor as shown in the photos. This dock aspect may be difficult to incorporate into the branding but the lake outline is included as an image applicable to include for that local reference aspect. We will be creating very high quality small batch liquors such as vodka, rum, gin and whiskey. Each batch will be triple distilled and perhaps 20 bottles in quantity so very exclusive. We are aiming at a premium feel for the branding. Attached are some bottle label designs that evoke the type of feel we are going for and a photo of the style of blank bottle to design for which is a 750ml Nordic pattern bottle.
In general we are going for more contemporary than traditional, more bold than delicate. If a single label the size desired would be 4 inches wide and 4 inches tall. If a double/split label as in two of the photos the top label would be 3 inches wide and 3 inches tall and the bottom label would be max 4 inches wide and 1.5 inches tall. We are open to the upper label being a "transparent" label to create a printed on bottle effect, perhaps of the brand logo. We are only interested in front label so do not require a back, neck or closure label. The label will require the ability to name the batch style name (example "Tuberix") and then the amplifying information for the type of alcohol (Russian Potato Vodka) in a smaller font. Another example ("Red Fox" and "London Dry Gin"). Information for bottle size (750ml) and alcohol % (40%) are also to be included. Governmental safety warnings are not required. We are open to use of any colours in the label. The basic label design would be re-used for different types of batches where we would change the style and alcohol name.
Updates

Target Market(s)

Up scale premium spirits buyers

Font styles to use
Serif
Sans Serif

Requirements
Must have
• A visual reference to the docks or the lake per the images attached.
Nice to have
• Ideally we can re-use the label design for a different type of Alcohol by changing the alcohol name and style information and maybe the colour of a major element in the label.

```html
<!DOCTYPE html>
<html lang="en">
<head>
<meta charset="utf-8">
<title>Seven Herons Distillery – Label System</title>
<link href="https://fonts.googleapis.com/css2?family=Montserrat:wght@700&family=Oswald:wght@500&family=Cabin:wght@700&display=swap" rel="stylesheet">
<style>
  :root {
    --paper: #f4f4f4;
    --label: #ffffff;
    --ink: #111111;
    --vodka: #f2d800;
    --gin: #f5a01a;
    --lake: #1a1a1a;
  }
  * { box-sizing: border-box; margin: 0; padding: 0; }
  html, body { width: 1200px; height: 849px; overflow: hidden; background: var(--paper); }
  .board { position: relative; width: 1200px; height: 849px; color: var(--ink); }

  .brand-mark {
    position: absolute; left: 0; top: 70px; width: 1200px; text-align: center;
    font-family: "Montserrat", sans-serif; font-weight: 700; letter-spacing: 4px;
  }
  .brand-mark .name { font-size: 46px; line-height: 1.1; }
  .brand-mark .kind { font-size: 30px; line-height: 1.2; margin-top: 14px; }

  .label {
    position: absolute; width: 403px; height: 401px; background: var(--label);
    box-shadow: 0 2px 8px rgba(0,0,0,.06);
  }
  .label-brand {
    position: absolute; top: 48px; left: 0; width: 100%; text-align: center;
    font-family: "Montserrat", sans-serif; font-weight: 700; letter-spacing: 2px;
  }
  .label-brand .name { font-size: 21px; }
  .label-brand .kind { font-size: 14px; margin-top: 10px; }
  .style-name {
    position: absolute; top: 178px; left: 0; width: 100%; text-align: center;
    font-family: "Oswald", sans-serif; font-weight: 500; font-size: 84px; line-height: 1;
    letter-spacing: 2px; color: var(--accent);
  }
  .spirit-type {
    position: absolute; top: 280px; left: 0; width: 100%; text-align: center;
    font-family: "Montserrat", sans-serif; font-weight: 700; font-size: 15.5px; letter-spacing: 2px;
  }
  .rule { position: absolute; height: 1.5px; width: 128px; background: var(--ink); }
  .rule.left { left: 0; } .rule.right { right: 0; }
  .rule.top { top: 348px; } .rule.bottom { top: 371px; }
  .spec {
    position: absolute; top: 349px; width: 128px; text-align: center;
    font-family: "Oswald", sans-serif; font-weight: 500; font-size: 15px; line-height: 22px;
  }
  .spec.abv { left: 0; } .spec.volume { right: 0; }
  .lake-mini {
    position: absolute; left: 175px; top: 337px; width: 52px; height: 18px;
    background: var(--lake); border-radius: 40% 60% 50% 50%;
  }
  .origin {
    position: absolute; top: 359px; left: 128px; width: 147px; text-align: center;
    font-family: "Cabin", sans-serif; font-weight: 700; font-size: 8.5px; line-height: 1.25;
  }

  .label.vodka { --accent: var(--vodka); }
  .label.gin { --accent: var(--gin); }
  .label.feature { left: 679px; top: 269px; }
  .label.thumb { top: 330px; transform: scale(.5); transform-origin: 0 0; }
  .label.thumb.vodka { left: 110px; }
  .label.thumb.gin { left: 345px; }

  .lake-outline {
    position: absolute; left: 545px; top: 702px; width: 112px; height: 66px;
    background: var(--lake); border-radius: 30% 70% 40% 60% / 60% 40% 60% 40%;
  }
  .origin-line {
    position: absolute; left: 0; top: 773px; width: 1200px; text-align: center;
    font-family: "Cabin", sans-serif; font-weight: 700; font-size: 19px; line-height: 1.25;
  }
</style>
</head>
<body>
<main class="board">
  <header class="brand-mark">
    <div class="name">SEVEN HERONS</div>
    <div class="kind">DISTILLERY</div>
  </header>

  <section class="label thumb vodka">
    <div class="label-brand"><div class="name">SEVEN HERONS</div><div class="kind">DISTILLERY</div></div>
    <div class="style-name">TUBERIX</div>
    <div class="spirit-type">RUSSIAN POTATO VODKA</div>
    <div class="rule left top"></div><div class="rule left bottom"></div>
    <div class="rule right top"></div><div class="rule right bottom"></div>
    <div class="spec abv">40% ALC</div><div class="spec volume">750 ML</div>
    <div class="lake-mini" role="img" aria-label="Outline map of Lac Vernisse"></div>
    <div class="origin">Distilled by Seven Herons Distillery<br>Quebec, Canada</div>
  </section>

  <section class="label thumb gin">
    <div class="label-brand"><div class="name">SEVEN HERONS</div><div class="kind">DISTILLERY</div></div>
    <div class="style-name">RED FOX</div>
    <div class="spirit-type">LONDON DRY GIN</div>
    <div class="rule left top"></div><div class="rule left bottom"></div>
    <div class="rule right top"></div><div class="rule right bottom"></div>
    <div class="spec abv">40% ALC</div><div class="spec volume">750 ML</div>
    <div class="lake-mini" role="img" aria-label="Outline map of Lac Vernisse"></div>
    <div class="origin">Distilled by Seven Herons Distillery<br>Quebec, Canada</div>
  </section>

  <section class="label feature vodka">
    <div class="label-brand"><div class="name">SEVEN HERONS</div><div class="kind">DISTILLERY</div></div>
    <div class="style-name">TUBERIX</div>
    <div class="spirit-type">RUSSIAN POTATO VODKA</div>
    <div class="rule left top"></div><div class="rule left bottom"></div>
    <div class="rule right top"></div><div class="rule right bottom"></div>
    <div class="spec abv">40% ALC</div><div class="spec volume">750 ML</div>
    <div class="lake-mini" role="img" aria-label="Outline map of Lac Vernisse"></div>
    <div class="origin">Distilled by Seven Herons Distillery<br>Quebec, Canada</div>
  </section>

  <div class="lake-outline" role="img" aria-label="Silhouette map of Lac Vernisse"></div>
  <p class="origin-line">Distilled by Seven Herons Distillery<br>Quebec, Canada</p>
</main>
</body>
</html>
```